Bayline Pet Rehoming GALA

Hi ALL!
We need an 8.5 X 11 inch, one page flyer to include all the below copy plus 8 sponsoring logos at the very bottom.
Thank YOU!

Corvel Heights Pet GALA
(Fun for Animals In Rescue!)

Sunday, August 12, 2018
1 to 4:30 p.m.

Animal Education & Adoption Event
featuring:

BK Pet Shelter & Services Rabbits & Mice

Hilltop Browsing Sheep

Thankful Hounds Haven

Featherwell Finches & Larks

Comet Pup Haven

Marla’s Feline Haven

Marvel Pup Haven

Special Guest from 1-3 p.m.
BeeBop - SF's 1st Therapy Pig!
Instagram: @BEEBOP_BKHOG
Facebook: @BEEBOP THE HOG

Activities for Kids
Dog & Cat Toy Making with Greta Vossel Canine Coaching
Animal Mask Making with Tiny Crafters
Face-in-a-Hole Photo Fun with Hugo Marsh Canine Coaching

BK PSS FREE Giveaway!
First 75 attending families receive a FREE PSS Doggie Bag containing a dog water bottle, food, shampoo, toy, treats and blinking dog collar light.

Animal Tails

1 pm Wendell’s Nook Storytime

1:30 p.m. BeeBop the Therapy Pig

1:45 pm “Tuft the Saved Hog”
Read by Author Marnie Oakhurst

2 p.m. Wendell’s Nook Singalong

2:30 p.m. Featherwell Finch Haven

2:45 p.m. Quire Pages Storytime

3 pm Browsing Sheep Refuge

3:15 p.m. The Burrow Den Puppet Show

3:45 pm BK PSS Officer Tamsin

4 p.m. Wendell’s Nook Storytime

Font styles to use
Serif

Colors

Designer to choose colors to be used in the design.

Requirements
Must have
• pig, goat, 2 dogs, kitten, dove, bunny

```html
<!DOCTYPE html>
<html lang="en">
<head>
<meta charset="utf-8">
<title>Corvel Heights Pet GALA – Flyers</title>
<link href="https://fonts.googleapis.com/css2?family=Arimo:wght@400;700&display=swap" rel="stylesheet">
<style>
:root{
  --orange:#f39c12;
  --purple:#4b2470;
  --ink:#2c2c2c;
  --grey:#6d6d6d;
  --rule:#d9d9d9;
  --backdrop:#e8e8e8;
  --paper:#ffffff;
}
*{box-sizing:border-box;margin:0;padding:0}
html,body{width:818px;height:1200px;overflow:hidden;background:var(--backdrop);font-family:"Arimo",Arial,sans-serif;color:var(--ink)}
.flyer{position:absolute;left:189px;width:440px;height:570px;background:var(--paper);box-shadow:0 3px 10px rgba(0,0,0,.18);overflow:hidden}
.flyer--front{top:20px}
.flyer--back{top:610px}
.abs{position:absolute}
.title{top:14px;left:0;width:100%;text-align:center;font-size:28px;font-weight:700;color:var(--orange);letter-spacing:.2px}
.subtitle{top:48px;left:0;width:100%;text-align:center;font-size:15px;color:var(--grey)}
.hero{top:70px;left:18px;width:404px;height:242px}
.event-name{top:318px;left:0;width:100%;text-align:center;font-size:17px;font-weight:700;color:var(--purple)}
.amp{color:var(--orange)}
.event-date{top:342px;left:0;width:100%;text-align:center;font-size:13px;font-weight:700;color:var(--ink)}
.event-time{top:359px;left:0;width:100%;text-align:center;font-size:13px;color:var(--ink)}
.feature-band{top:382px;left:0;width:168px;height:26px}
.feature-label{top:385px;left:20px;font-size:19px;font-weight:700;color:#fff}
.feature-list{top:416px;left:20px;list-style:none;font-size:8.6px;line-height:13px;color:var(--ink)}
.feature-list li::before{content:"";display:inline-block;width:4px;height:4px;border-radius:50%;background:var(--orange);margin-right:7px;vertical-align:middle}
.circles{top:400px;left:198px;width:236px;height:112px}
.guest{top:506px;left:24px;width:262px;height:22px}
.guest-text{top:510px;left:34px;font-size:13px;color:var(--orange);font-weight:700}
.guest-text span{color:var(--grey);font-weight:400}
.footer{top:530px;left:0;width:440px;height:40px;display:flex}
.footer-name{width:265px;background:var(--orange);color:#fff;font-size:16px;font-weight:700;display:flex;align-items:center;padding-left:20px}
.footer-social{flex:1;background:var(--purple);color:#fff;font-size:10.5px;display:flex;flex-direction:column;justify-content:center;padding-left:32px;gap:4px}
.footer-social div{display:flex;align-items:center;gap:8px}
.footer-social i{display:inline-block;width:9px;height:9px;background:#fff;border-radius:2px}
.head{font-size:14.5px;font-weight:700;color:var(--orange)}
.head span{color:var(--purple);font-weight:400}
.body-copy{font-size:7.6px;line-height:10px;color:var(--ink);text-align:justify}
.kids-head{top:314px;left:16px}
.kids-copy{top:334px;left:16px;width:206px}
.give-head{top:390px;left:16px}
.give-copy{top:410px;left:16px;width:206px}
.kid-circles{top:446px;left:16px;width:200px;height:78px}
.tails-head{top:314px;left:236px}
.schedule{position:absolute;left:236px;width:192px;border-collapse:collapse;font-size:7.8px}
.schedule td{border:1px solid var(--rule);height:16px;padding:0 5px;font-weight:700}
.schedule .time{width:50px;color:var(--orange)}
.schedule .act{color:var(--ink)}
.schedule--early{top:333px}
.schedule--late{top:421px}
.read-by{top:384px;left:236px;font-size:12px;color:var(--purple)}
.author{top:399px;left:236px;font-size:12px;font-weight:700;color:var(--orange)}
</style>
</head>
<body>

<section class="flyer flyer--front">
  <h1 class="abs title">Corvel Heights Pet GALA</h1>
  <p class="abs subtitle">(Fun for Animals In Rescue!)</p>
  <svg class="abs hero" viewBox="0 0 404 242" role="img" aria-label="Photo of a woman hugging a happy beagle beside a bright window">
    <defs><linearGradient id="heroFront" x1="0" y1="0" x2="1" y2="1"><stop offset="0" stop-color="#9db07a"/><stop offset=".45" stop-color="#e9dcc8"/><stop offset="1" stop-color="#c9b39a"/></linearGradient></defs>
    <path d="M30 30 Q60 8 110 14 Q160 2 210 10 Q270 0 320 12 Q380 8 392 50 Q404 100 396 150 Q402 200 370 222 Q320 240 260 232 Q200 242 140 234 Q80 240 40 220 Q6 200 10 150 Q0 100 14 60 Q16 40 30 30Z" fill="url(#heroFront)"/>
  </svg>
  <h2 class="abs event-name">ANIMAL EDUCATION <span class="amp">&amp;</span> ADOPTION EVENT</h2>
  <p class="abs event-date">SUNDAY, &nbsp;12 <span class="amp">AUGUST</span> 2018</p>
  <p class="abs event-time">1P.M TO 4:30 P.M.</p>
  <svg class="abs feature-band" viewBox="0 0 168 26"><polygon points="0,0 140,0 152,26 0,26" fill="var(--purple)"/><polygon points="142,0 154,0 166,26 154,26" fill="var(--orange)"/></svg>
  <p class="abs feature-label">Featuring</p>
  <ul class="abs feature-list">
    <li>BK Pet Shelter &amp; Services Rabbits &amp; Mice</li>
    <li>Hilltop Browsing Sheep</li>
    <li>Thankful Hounds Haven</li>
    <li>Featherwell Finches &amp; Larks</li>
    <li>Comet Pup Haven</li>
    <li>Marla’s Feline Haven</li>
    <li>Marvel Pup Haven</li>
  </ul>
  <svg class="abs circles" viewBox="0 0 236 112">
    <circle cx="118" cy="52" r="52" fill="none" stroke="var(--orange)" stroke-dasharray="2 3"/>
    <circle cx="40" cy="62" r="37" fill="none" stroke="var(--orange)" stroke-dasharray="2 3"/>
    <circle cx="196" cy="62" r="37" fill="none" stroke="var(--orange)" stroke-dasharray="2 3"/>
    <circle cx="40" cy="62" r="33" fill="#c9c99a" role="img" aria-label="Photo of a white dove on grass"/>
    <circle cx="118" cy="52" r="47" fill="#7b7468" role="img" aria-label="Photo of a small black and white pig"/>
    <circle cx="196" cy="62" r="33" fill="#8fa4a8" role="img" aria-label="Photo of a white goat"/>
  </svg>
  <svg class="abs guest" viewBox="0 0 262 22"><polygon points="0.5,0.5 252,0.5 261.5,21.5 0.5,21.5" fill="none" stroke="#9a9a9a"/></svg>
  <p class="abs guest-text">Special Guest <span>From 1p.m -3 P.m.</span></p>
  <footer class="abs footer">
    <div class="footer-name">BeeBop - SF's 1st Therapy Pig!</div>
    <div class="footer-social"><div><i></i>@BEEBOP_BKHOG</div><div><i></i>@BEEBOP THE HOG</div></div>
  </footer>
</section>

<section class="flyer flyer--back">
  <h1 class="abs title">Corvel Heights Pet GALA</h1>
  <p class="abs subtitle">(Fun for Animals In Rescue!)</p>
  <svg class="abs hero" viewBox="0 0 404 242" role="img" aria-label="Photo of a woman in a sweater playing with a ginger cat at home">
    <defs><linearGradient id="heroBack" x1="0" y1="0" x2="1" y2="1"><stop offset="0" stop-color="#5a5e6b"/><stop offset=".45" stop-color="#c9a07a"/><stop offset="1" stop-color="#ece7e1"/></linearGradient></defs>
    <path d="M26 36 Q56 6 110 12 Q170 0 220 10 Q280 2 330 14 Q386 14 394 60 Q404 110 392 160 Q398 210 360 226 Q310 242 250 232 Q190 242 130 234 Q70 240 36 214 Q4 190 12 140 Q2 90 14 62 Q14 46 26 36Z" fill="url(#heroBack)"/>
  </svg>
  <h2 class="abs head kids-head">ACTIVITIES <span>FOR KIDS</span></h2>
  <p class="abs body-copy kids-copy">Dog &amp; Cat Toy Making with Greta Vossel Canine Coaching. Animal Mask Making with Tiny Crafters. Face-in-a-Hole Photo Fun with Hugo Marsh Canine Coaching.</p>
  <h2 class="abs head give-head">BK PSS FREE <span>Giveaway!</span></h2>
  <p class="abs body-copy give-copy">First 75 attending families receive a FREE PSS Doggie Bag containing a dog water bottle, food, shampoo, toy, treats and blinking dog collar light.</p>
  <svg class="abs kid-circles" viewBox="0 0 200 78">
    <circle cx="100" cy="40" r="37" fill="none" stroke="var(--orange)" stroke-dasharray="2 3"/>
    <circle cx="36" cy="46" r="30" fill="none" stroke="var(--orange)" stroke-dasharray="2 3"/>
    <circle cx="164" cy="46" r="30" fill="none" stroke="var(--orange)" stroke-dasharray="2 3"/>
    <circle cx="36" cy="46" r="26" fill="#e6dcc2" role="img" aria-label="Photo of a small bunny"/>
    <circle cx="100" cy="40" r="33" fill="#b98a5e" role="img" aria-label="Photo of two kittens"/>
    <circle cx="164" cy="46" r="26" fill="#7fa260" role="img" aria-label="Photo of two dogs running on grass"/>
  </svg>
  <h2 class="abs head tails-head">ANIMAL <span>TAILS</span></h2>
  <table class="schedule schedule--early">
    <tr><td class="time">1 pm</td><td class="act">Wendell’s Nook Storytime</td></tr>
    <tr><td class="time">1:30 p.m.</td><td class="act">BeeBop the Therapy Pig</td></tr>
    <tr><td class="time">1:45 pm</td><td class="act">“Tuft the Saved Hog”</td></tr>
  </table>
  <p class="abs read-by">READ BY</p>
  <p class="abs author">AUTHOR MARNIE OAKHURST</p>
  <table class="schedule schedule--late">
    <tr><td class="time">2 p.m.</td><td class="act">Wendell’s Nook Singalong</td></tr>
    <tr><td class="time">2:30 p.m.</td><td class="act">Featherwell Finch Haven</td></tr>
    <tr><td class="time">2:45 p.m.</td><td class="act">Quire Pages Storytime</td></tr>
    <tr><td class="time">3 pm</td><td class="act">Browsing Sheep Refuge</td></tr>
    <tr><td class="time">3:15 p.m.</td><td class="act">The Burrow Den Puppet Show</td></tr>
    <tr><td class="time">3:45 pm</td><td class="act">BK PSS Officer Tamsin</td></tr>
  </table>
  <footer class="abs footer">
    <div class="footer-name">BeeBop - SF's 1st Therapy Pig!</div>
    <div class="footer-social"><div><i></i>@BEEBOP_BKHOG</div><div><i></i>@BEEBOP THE HOG</div></div>
  </footer>
</section>

</body>
</html>
```